PennaForms Web Page

This is a simple, one page design. I have attached a mockup in Word along with the PennaForms and BriskSheets logos.

The layout does not need to be recreated, but the fonts/colors might need improvement.

The firm information at the bottom definitely needs help.

Thanks.

```html
<!DOCTYPE html>
<html lang="en">
<head>
<meta charset="utf-8">
<title>PennaForms – Document Automation</title>
<link rel="stylesheet" href="https://fonts.googleapis.com/css2?family=PT+Sans:ital,wght@0,400;0,700;1,400&family=Roboto:wght@400;500;700&family=Raleway:wght@400&display=swap">
<style>
:root{
  --navy:#123a6e;
  --navy-dark:#0b1c33;
  --blue:#2a86e0;
  --blue-deep:#1d4f8e;
  --yellow:#f5dc1a;
  --red:#c9413a;
  --red-dark:#a8322c;
  --ink:#111;
  --grey-text:#6d6d6d;
  --band:#ececec;
  --line:#e6e6e6;
  --white:#fff;
  --footer-text:#e9eef6;
  --bottom-bar:#141414;
}
*{margin:0;padding:0;box-sizing:border-box}
html,body{width:902px;height:1200px;overflow:hidden;background:var(--white)}
body{position:relative;font-family:"PT Sans",Arial,sans-serif;color:var(--ink)}
.abs{position:absolute}

/* header */
.brand{left:123px;top:30px;display:flex;align-items:center;gap:8px}
.brand-mark{width:18px;height:18px;background:var(--navy)}
.brand-name{font-family:"PT Sans",sans-serif;font-weight:700;font-size:27px;color:var(--navy)}
.callout{right:123px;top:34px;text-align:right;font-family:"Roboto",sans-serif}
.callout .label{font-size:10px;color:#777;letter-spacing:.5px}
.callout .phone{font-size:14px;font-weight:700;color:#444;margin-top:3px}

/* nav */
.nav-bar{left:0;top:85px;width:902px;height:43px;background:linear-gradient(90deg,var(--navy-dark),#163a66 45%,#1b467a 70%,var(--navy-dark))}
.nav-link{top:85px;height:43px;line-height:43px;font-family:"Roboto",sans-serif;font-weight:500;font-size:11px;color:var(--white)}
.nav-link.is-active{background:var(--blue);width:73px;text-align:center}
.search-btn{left:737px;top:85px;width:42px;height:43px;background:var(--blue);display:flex;align-items:center;justify-content:center}
.submenu{left:289px;top:129px;width:143px;background:#f6f6f6;border:1px solid #ddd;z-index:5}
.submenu a{display:block;height:24px;line-height:24px;padding-left:9px;font-size:9px;color:#777;text-decoration:none;border-bottom:1px solid #e8e8e8}
.submenu a.is-hover{font-weight:700;color:#333}

/* hero */
.hero{left:123px;top:148px;width:656px;height:283px;background:radial-gradient(ellipse at 55% 35%,#2a5fa4 0%,#1c4886 45%,#123564 100%);text-align:center;color:var(--white)}
.hero-kicker{position:absolute;left:0;right:0;top:74px;font-weight:700;font-size:28px;letter-spacing:.3px}
.hero-title{position:absolute;left:0;right:0;top:98px;font-weight:700;font-size:58px;color:var(--yellow);line-height:1}
.hero-sub{position:absolute;left:0;right:0;top:162px;font-family:"Raleway",sans-serif;font-size:16px}
.hero-btn{position:absolute;left:265px;top:196px;width:126px;height:24px;line-height:24px;background:linear-gradient(#3a8fe6,#1f6ec4);font-family:"Roboto",sans-serif;font-weight:500;font-size:9px;border-radius:2px}
.hero-arrow{top:268px;width:22px;height:43px;display:flex;align-items:center;justify-content:center}
.hero-arrow.prev{left:123px;background:#0b0b0b}
.hero-arrow.next{left:757px;background:var(--blue)}

/* welcome band */
.welcome{left:123px;top:453px;width:656px;height:76px;background:var(--band)}
.welcome h2{position:absolute;left:23px;top:24px;font-family:"Roboto",sans-serif;font-weight:500;font-size:14px;color:#222}
.welcome p{position:absolute;left:23px;top:43px;font-size:9.5px;color:var(--grey-text)}
.btn-red{background:linear-gradient(#d24b43,var(--red-dark));color:var(--white);font-family:"Roboto",sans-serif;font-weight:500;font-size:9px;text-align:center;border-radius:2px}
.welcome .btn-red{position:absolute;left:504px;top:26px;width:126px;height:25px;line-height:25px}

/* features */
.feature-icon{width:48px;height:48px;border-radius:50%;background:var(--navy);display:flex;align-items:center;justify-content:center}
.feature-icon.is-accent{background:var(--red)}
.feature-text{width:290px}
.feature-text h3{font-family:"Roboto",sans-serif;font-weight:700;font-size:9px;margin-bottom:5px}
.feature-text p{font-size:9.5px;line-height:15px;color:var(--grey-text)}
.divider{left:123px;top:686px;width:656px;height:1px;background:var(--line)}
.divider-dots{left:440px;top:684px;font-size:8px;letter-spacing:2px;color:#ccc;line-height:4px}

/* blog */
.section-title{font-family:"Roboto",sans-serif;font-weight:500;font-size:11px;color:#111}
.post{top:746px;width:148px}
.post-thumb{height:83px}
.post h4{margin-top:14px;font-family:"Roboto",sans-serif;font-weight:700;font-size:9px}
.post p{margin-top:6px;font-size:9.5px;line-height:14.5px;color:var(--grey-text)}
.post .meta{margin-top:9px;font-size:8.5px;font-style:italic;color:#777;padding-left:3px}
.post .meta b{font-weight:700;color:#222}

/* footer */
.footer{left:0;top:968px;width:902px;height:197px;background:linear-gradient(160deg,#0f2b52 0%,#1c4b8a 40%,#163e72 70%,#0e2a50 100%)}
.footer-col{top:990px;color:var(--footer-text);font-size:9px}
.footer-col h5{font-family:"Roboto",sans-serif;font-weight:500;font-size:11px;color:var(--white);margin-bottom:21px}
.footer-col .body{line-height:14.5px}
.dropcap{float:left;font-family:"Roboto",sans-serif;font-weight:700;font-size:28px;line-height:26px;margin-right:10px;color:var(--white)}
.footer-col ul{list-style:none}
.footer-col li{line-height:19.5px}
.footer-col li.is-current{color:var(--blue)}
.tweet-time{font-size:7px;color:var(--blue);margin-top:2px}
.footer-btn{top:1108px;height:24px;line-height:24px}
.btn-dark{background:linear-gradient(#333,#0c0c0c);color:var(--white);font-family:"Roboto",sans-serif;font-weight:500;font-size:9px;text-align:center;border-radius:2px}
.bottom-bar{left:0;top:1165px;width:902px;height:35px;background:var(--bottom-bar)}
.copyright{left:125px;top:1176px;font-size:9px;color:#777}
</style>
</head>
<body>

<!-- header -->
<div class="abs brand"><span class="brand-mark"></span><span class="brand-name">PennaForms</span></div>
<div class="abs callout"><div class="label">Free Call Us:</div><div class="phone">+900 555 01 23</div></div>

<!-- navigation -->
<div class="abs nav-bar"></div>
<a class="abs nav-link is-active" style="left:123px">Home</a>
<a class="abs nav-link" style="left:222px">About Us</a>
<a class="abs nav-link" style="left:315px">Services</a>
<a class="abs nav-link" style="left:406px">Products</a>
<a class="abs nav-link" style="left:498px">Blog</a>
<a class="abs nav-link" style="left:570px">Contact</a>
<div class="abs search-btn">
  <svg width="14" height="14" viewBox="0 0 14 14"><circle cx="5.5" cy="5.5" r="4" fill="none" stroke="#fff" stroke-width="2"/><line x1="8.5" y1="8.5" x2="13" y2="13" stroke="#fff" stroke-width="2.4" stroke-linecap="round"/></svg>
</div>
<nav class="abs submenu">
  <a href="#">Sub menu text</a>
  <a href="#" class="is-hover">Sub menu text</a>
  <a href="#">Sub menu text</a>
</nav>

<!-- hero slider -->
<section class="abs hero" role="img" aria-label="Blue abstract curved backdrop behind the headline">
  <div class="hero-kicker">DOCUMENT AUTOMATION FOR THE</div>
  <div class="hero-title">21ST CENTURY</div>
  <div class="hero-sub">Lorem Ipsum is simply a dummy text</div>
  <div class="hero-btn">read more</div>
</section>
<div class="abs hero-arrow prev"><svg width="8" height="12" viewBox="0 0 8 12"><polyline points="6,1 2,6 6,11" fill="none" stroke="#fff" stroke-width="1.5"/></svg></div>
<div class="abs hero-arrow next"><svg width="8" height="12" viewBox="0 0 8 12"><polyline points="2,1 6,6 2,11" fill="none" stroke="#fff" stroke-width="1.5"/></svg></div>

<!-- welcome band -->
<section class="abs welcome">
  <h2>Welcome to our website</h2>
  <p>Contrary to popular belief, Lorem Ipsum is not simply random text. It has roots in a piece of classical Latin</p>
  <div class="btn-red">Download Brochure</div>
</section>

<!-- features -->
<div class="abs feature-icon" style="left:123px;top:555px">
  <svg width="20" height="20" viewBox="0 0 20 20"><rect x="4" y="2" width="12" height="16" fill="none" stroke="#fff" stroke-width="1.6"/><line x1="7" y1="7" x2="13" y2="7" stroke="#fff" stroke-width="1.4"/><line x1="7" y1="10" x2="13" y2="10" stroke="#fff" stroke-width="1.4"/><line x1="7" y1="13" x2="11" y2="13" stroke="#fff" stroke-width="1.4"/></svg>
</div>
<div class="abs feature-text" style="left:180px;top:552px"><h3>Lorem Ipsum is Dummy</h3><p>Contrary to popular belief, Lorem Ipsum is not simply random text.<br>It has roots in a piece of classical Latin</p></div>

<div class="abs feature-icon" style="left:461px;top:555px">
  <svg width="22" height="20" viewBox="0 0 22 20"><path d="M2 5h6l2 2h9v10H2z" fill="#fff"/><rect x="6" y="2" width="10" height="7" fill="none" stroke="#fff" stroke-width="1.3"/></svg>
</div>
<div class="abs feature-text" style="left:518px;top:552px"><h3>Lorem Ipsum is Dummy</h3><p>Contrary to popular belief, Lorem Ipsum is not simply random text.<br>It has roots in a piece of classical Latin</p></div>

<div class="abs feature-icon" style="left:123px;top:615px">
  <svg width="22" height="18" viewBox="0 0 22 18"><rect x="2" y="3" width="18" height="13" fill="#fff"/><polyline points="2,3 11,10 20,3" fill="none" stroke="#123a6e" stroke-width="1.5"/></svg>
</div>
<div class="abs feature-text" style="left:180px;top:618px"><h3>Lorem Ipsum is Dummy</h3><p>Contrary to popular belief, Lorem Ipsum is not simply random text.<br>It has roots in a piece of classical Latin</p></div>

<div class="abs feature-icon is-accent" style="left:461px;top:615px">
  <svg width="20" height="20" viewBox="0 0 20 20"><path d="M4 2h8l4 4v12H4z" fill="none" stroke="#fff" stroke-width="1.5"/><path d="M7 14c2-5 3-7 3-9 0 3 2 6 4 7-3 0-5 1-7 2z" fill="none" stroke="#fff" stroke-width="1.1"/></svg>
</div>
<div class="abs feature-text" style="left:518px;top:618px"><h3>Lorem Ipsum is Dummy</h3><p>Contrary to popular belief, Lorem Ipsum is not simply random text.<br>It has roots in a piece of classical Latin</p></div>

<div class="abs divider"></div>
<div class="abs divider-dots">····</div>

<!-- blog -->
<h3 class="abs section-title" style="left:125px;top:711px">Recent Blog Post</h3>

<article class="abs post" style="left:123px">
  <div class="post-thumb" role="img" aria-label="Red file folders, shown with a hover overlay" style="background:linear-gradient(135deg,#e0655a,#d14a40)"></div>
  <h4>Lorem Ipsum</h4>
  <p>Contrary to popular belief, Lorem Ipsum is not simply random text. It has roots in a piece of classical Latin</p>
  <div class="meta">In <b>Standart</b> // May 12 , 2012</div>
</article>
<article class="abs post" style="left:292px">
  <div class="post-thumb" role="img" aria-label="Hands reviewing paperwork at a desk with a keyboard" style="background:linear-gradient(135deg,#e8edf2,#9aa4ae)"></div>
  <h4>Lorem Ipsum</h4>
  <p>Contrary to popular belief, Lorem Ipsum is not simply random text. It has roots in a piece of classical Latin</p>
  <div class="meta">In <b>Standart</b> // May 12 , 2012</div>
</article>
<article class="abs post" style="left:462px">
  <div class="post-thumb" role="img" aria-label="Row of coloured ring binders" style="background:linear-gradient(90deg,#3a3a3e,#c45560 55%,#5a4f9e)"></div>
  <h4>Lorem Ipsum</h4>
  <p>Contrary to popular belief, Lorem Ipsum is not simply random text. It has roots in a piece of classical Latin</p>
  <div class="meta">In <b>Standart</b> // May 12 , 2012</div>
</article>
<article class="abs post" style="left:630px">
  <div class="post-thumb" role="img" aria-label="Hand holding a blue folder beside stacked documents" style="background:linear-gradient(135deg,#c84b3e,#2a56a8 55%,#1e4a9a)"></div>
  <h4>Lorem Ipsum</h4>
  <p>Contrary to popular belief, Lorem Ipsum is not simply random text. It has roots in a piece of classical Latin</p>
  <div class="meta">In <b>Standart</b> // May 12 , 2012</div>
</article>

<!-- footer -->
<footer class="abs footer"></footer>
<div class="abs footer-col" style="left:125px;width:150px">
  <h5>About Us</h5>
  <div class="body"><span class="dropcap">Q</span>Lorem ipsum ex vix illud dem tation et his. At vix scripta patri Lorem ipsum ex vix illud tation et his. At vix scripta patrioque</div>
</div>
<div class="abs footer-col" style="left:404px;width:150px">
  <h5>Chirper Widget</h5>
  <div class="body">The Big Tent was in the Big Apple yesterday to discuss the Internet's impact on arts &amp; culture http://EXAMPLE/123456</div>
  <div class="tweet-time">about 15 hours ago</div>
</div>
<div class="abs footer-col" style="left:677px;width:110px">
  <h5>Recent Blog Post</h5>
  <ul>
    <li>Patrioque scribentur</li>
    <li>Novum tation et his</li>
    <li>Scripta patrioque</li>
    <li class="is-current">Electronic Commerce</li>
    <li>Class aptent taciti sociosqu</li>
  </ul>
</div>
<div class="abs footer-btn btn-red" style="left:123px;width:85px">read more</div>
<div class="abs footer-btn btn-dark" style="left:405px;width:86px">read more</div>

<div class="abs bottom-bar"></div>
<div class="abs copyright">© Copyright 2014 PennaForms</div>

</body>
</html>
```